Leeward Health Academy Open House

We need to create an advertisement for an upcoming open house that we are conducting. We can create a design in the dimensions of 10" (w) x 13.67" (h). Once that is approved, I will need the ad resized in the following dimensions:

8.5" (w) x 11" (h) - PDF
2400 pixels wide X 2400 pixels height - JPEG

Target Market(s)

Aspiring medical students

Industry/Entity Type

Medical

Requirements
Must have
• Logo
• Tag line: STUDY MEDICINE IN THE CARIBBEAN, BECOME A DOC IN THE US
• One of the attachments has a JPEG file with all the information to include in this new ad however the event location has changed to this:
• Sunday, April 22nd at 1pm at:
• Bramblewood Suites Chicago Quay Court
• 712 N. Fenwick Drive
• Chicago, IL 60687
• Event will be held on the 15th floor in The Osgood Room
• FREE parking. Refreshments will be served.
• Change email to admissions@lhamedic.org
• Use a nice background and creative design. The details of the event need to be big and emphasize OPEN HOUSE.

```html
<!DOCTYPE html>
<html lang="en">
<head>
<meta charset="utf-8">
<title>Leeward Health Academy – Open House</title>
<link href="https://fonts.googleapis.com/css2?family=Graduate&family=Russo+One&family=Roboto+Condensed:wght@400;700&family=Open+Sans:ital,wght@1,700&display=swap" rel="stylesheet">
<style>
  :root {
    --sky: #0eaaea;
    --sky-deep: #0a86cf;
    --sky-soft: #45c1f2;
    --yellow: #fbc723;
    --white: #ffffff;
    --navy: #1d2d4f;
    --cap: #1f2740;
    --red: #e8322f;
    --orange: #f4722b;
    --footer-orange: #f08a24;
    --footer-red: #d7262c;
  }
  * { margin: 0; padding: 0; box-sizing: border-box; }
  html, body { width: 888px; height: 1200px; overflow: hidden; }
  body { background: var(--sky); font-family: "Roboto Condensed", sans-serif; }
  .flyer {
    position: relative; width: 888px; height: 1200px; overflow: hidden;
    background: radial-gradient(ellipse at 85% 30%, var(--sky-soft) 0%, var(--sky) 45%), var(--sky);
  }
  .shapes { position: absolute; inset: 0; }

  .tagline {
    position: absolute; left: 138px; top: 86px; white-space: nowrap;
    font-family: "Russo One", sans-serif; font-weight: 400; color: var(--white);
    font-size: 37px; line-height: 44px;
  }
  .tagline .sub { display: block; color: var(--yellow); font-size: 25px; line-height: 32px; }

  .brand {
    position: absolute; left: 634px; top: 53px; width: 198px; height: 198px;
    border-radius: 50%; background: var(--white);
    display: flex; align-items: center; justify-content: center; text-align: center;
    font-family: "Russo One", sans-serif; color: var(--navy); font-size: 21px; line-height: 28px;
  }

  .frame {
    position: absolute; left: 189px; top: 282px; width: 539px; height: 521px;
    border: 9px solid var(--white);
  }
  .headline {
    position: absolute; left: 189px; top: 412px; width: 539px; text-align: center;
    font-family: "Graduate", sans-serif; font-weight: 400; color: var(--yellow);
    font-size: 104px; line-height: 112px;
    transform: scaleY(1.32); transform-origin: top center;
  }

  .date { position: absolute; left: 74px; top: 846px; color: var(--white); width: 170px; height: 130px; }
  .date .day { position: absolute; left: 0; top: 0; font-size: 23px; font-weight: 700; line-height: 26px; }
  .date .num { position: absolute; left: 0; top: 24px; font-size: 78px; font-weight: 700; line-height: 78px; }
  .date .suffix { position: absolute; left: 84px; top: 30px; font-size: 18px; line-height: 22px; }
  .date .time { position: absolute; left: 0; top: 96px; font-size: 23px; line-height: 26px; }

  .venue {
    position: absolute; left: 325px; top: 832px; color: var(--white); font-style: normal;
    font-size: 29px; line-height: 29px;
  }
  .venue .name { display: block; font-weight: 700; font-size: 30px; }

  .floor { position: absolute; left: 644px; top: 856px; width: 200px; height: 140px; color: var(--navy); }
  .floor .lead { position: absolute; left: 0; top: 0; font-size: 24px; line-height: 24px; }
  .floor .num { position: absolute; left: 0; top: 46px; color: var(--white); font-size: 76px; font-weight: 700; line-height: 72px; }
  .floor .th { position: absolute; left: 114px; top: 56px; color: var(--white); font-size: 25px; line-height: 26px; }
  .floor .in { position: absolute; left: 101px; top: 90px; color: var(--white); font-size: 25px; line-height: 26px; }
  .floor .room { position: absolute; left: 0; top: 118px; color: var(--white); font-weight: 700; font-size: 25px; line-height: 26px; white-space: nowrap; }

  .rule { position: absolute; left: 64px; width: 757px; height: 2px; background: rgba(255,255,255,.75); }
  .rule.top { top: 1028px; }
  .rule.bottom { top: 1105px; }
  .perks {
    position: absolute; left: 64px; top: 1043px; width: 757px; text-align: center;
    color: var(--white); font-size: 38px; line-height: 50px;
  }
  .perks .sep { margin: 0 26px; }

  .footer {
    position: absolute; left: 0; top: 1137px; width: 888px; height: 63px; background: var(--white);
    display: flex; justify-content: space-between; align-items: center; padding: 0 64px;
    font-family: "Open Sans", sans-serif; font-style: italic; font-weight: 700; font-size: 24px;
  }
  .footer .email { color: var(--footer-orange); }
  .footer .web { color: var(--footer-red); }
</style>
</head>
<body>
<main class="flyer">
  <svg class="shapes" width="888" height="1200" viewBox="0 0 888 1200">
    <defs>
      <linearGradient id="venue-stroke" x1="0" x2="1">
        <stop offset="0" stop-color="var(--red)"/><stop offset="1" stop-color="var(--orange)"/>
      </linearGradient>
    </defs>
    <path class="tagline-stroke" d="M100 70 L640 52 L630 232 L180 250 L110 210 Z" fill="var(--sky-deep)" opacity=".7"/>
    <path class="date-stroke" d="M40 800 L250 795 L258 985 L34 980 L24 880 Z" fill="var(--red)"/>
    <path class="venue-stroke" d="M248 812 L628 800 L620 990 L255 1002 Z" fill="url(#venue-stroke)"/>
    <g fill="var(--cap)">
      <rect role="img" aria-label="Graduation cap tossed in the air" x="180" y="325" width="170" height="90" rx="8" transform="rotate(-10 265 370)"/>
      <rect role="img" aria-label="Graduation cap tossed in the air" x="600" y="300" width="140" height="105" rx="8" transform="rotate(14 670 352)"/>
      <rect role="img" aria-label="Graduation cap tossed in the air" x="110" y="570" width="140" height="85" rx="8" opacity=".45" transform="rotate(-8 180 612)"/>
      <rect role="img" aria-label="Graduation cap tossed in the air" x="206" y="705" width="100" height="110" rx="8" transform="rotate(10 256 760)"/>
      <rect role="img" aria-label="Graduation cap tossed in the air" x="540" y="712" width="190" height="80" rx="8" transform="rotate(-8 635 752)"/>
    </g>
  </svg>

  <h1 class="tagline">STUDY MEDICINE IN<br>THE CARIBBEAN,<span class="sub">BECOME A DOC IN THE US</span></h1>

  <div class="brand">Leeward<br>Health<br>Academy</div>

  <div class="frame"></div>
  <h2 class="headline">OPEN<br>HOUSE</h2>

  <div class="date">
    <span class="day">SUNDAY</span>
    <span class="num">22</span>
    <span class="suffix">nd<br>April</span>
    <span class="time">@ 1pm</span>
  </div>

  <address class="venue">
    <span class="name">Bramblewood Suites</span>
    Chicago Quay Court<br>712 N. Fenwick Drive<br>Chicago, IL 60687
  </address>

  <div class="floor">
    <span class="lead">Event will be<br>held on the</span>
    <span class="num">15</span>
    <span class="th">th floor</span>
    <span class="in">in The</span>
    <span class="room">Osgood Room</span>
  </div>

  <div class="rule top"></div>
  <p class="perks">FREE parking<span class="sep">|</span>Refreshments will be served</p>
  <div class="rule bottom"></div>

  <footer class="footer">
    <span class="email">admissions@lhamedic.org</span>
    <span class="web">www.lhamedic.org</span>
  </footer>
</main>
</body>
</html>
```